Design a book cover
TItle: Where Did Mercy Wander?
Suggested graphic: Jesus holding a gun
Subtitle: A public defender's views on the death penalty
Author Name: Curtis Vanbrook

```html
<!DOCTYPE html>
<html lang="en">
<head>
<meta charset="utf-8">
<title>Where Did Mercy Wander? — Book Cover</title>
<link href="https://fonts.googleapis.com/css2?family=Poppins:wght@300;400;800&display=swap" rel="stylesheet">
<style>
  :root {
    --backdrop: #5a5a5c;
    --paper: #f7efe0;
    --ink: #0b0f0f;
    --accent: #e4852a;
    --accent-deep: #c46f22;
  }
  html, body {
    margin: 0;
    padding: 0;
    width: 1200px;
    height: 1200px;
    overflow: hidden;
    background: var(--backdrop);
  }
  .book-cover {
    position: absolute;
    left: 217px;
    top: 42px;
    width: 766px;
    height: 1088px;
    background: var(--paper);
    overflow: hidden;
    font-family: "Poppins", sans-serif;
  }
  .title {
    position: absolute;
    top: 36px;
    left: 0;
    width: 100%;
    margin: 0;
    text-align: center;
    color: var(--ink);
    font-weight: 800;
    line-height: 1;
    letter-spacing: -0.5px;
  }
  .title-line-one {
    display: block;
    font-size: 62px;
  }
  .title-line-two {
    display: block;
    font-size: 76px;
    margin-top: 8px;
  }
  .title-accent {
    color: var(--accent);
  }
  .subtitle {
    position: absolute;
    top: 184px;
    left: 0;
    width: 100%;
    margin: 0;
    text-align: center;
    color: var(--ink);
    font-weight: 300;
    font-size: 24px;
    line-height: 36px;
    letter-spacing: 0.5px;
    text-transform: uppercase;
  }
  .cover-illustration {
    position: absolute;
    left: 118px;
    top: 250px;
    width: 510px;
    height: 708px;
    z-index: 2;
    border-radius: 255px 255px 40px 40px / 240px 240px 40px 40px;
    background: linear-gradient(180deg, var(--accent) 0%, var(--accent-deep) 70%, #3a2a1a 100%);
  }
  .author-band {
    position: absolute;
    left: 0;
    bottom: 0;
    width: 100%;
    height: 164px;
    background: var(--ink);
    z-index: 1;
  }
  .author-name {
    position: absolute;
    left: 0;
    top: 66px;
    width: 100%;
    margin: 0;
    text-align: center;
    color: var(--paper);
    font-weight: 400;
    font-size: 34px;
    line-height: 1.5;
    text-transform: uppercase;
    letter-spacing: 0.5px;
    z-index: 3;
  }
</style>
</head>
<body>
  <main class="book-cover">
    <h1 class="title">
      <span class="title-line-one">WHERE DID</span>
      <span class="title-line-two"><span class="title-accent">MERCY</span> WANDER?</span>
    </h1>
    <p class="subtitle">A public defender's views on the death penalty</p>
    <div class="cover-illustration" role="img" aria-label="Cover illustration in orange, cream and black"></div>
    <footer class="author-band">
      <p class="author-name">Curtis Vanbrook</p>
    </footer>
  </main>
</body>
</html>
```